Healthcare IT company looking for business card design

We develop IT systems for healthcare that significantly reduces cost and improves quality.

We want a business card design that is professional and clean, and using the colors in our logo.

Target Market(s)

Doctors and decision makers in the healthcare industry

Industry/Entity Type

Healthcare

Contact Information for Business Card

It should include
Name and title, address, telephone

Tobias Vrenholt, CEO
+46 712 418257
tobias@kelvaro.se

Font styles to use
Serif

Colors
0355a3
ed282f

Requirements
Must have
• Clean design
• Professional feel
Nice to have
• N/A
Should not have
• N/A

```html
<!DOCTYPE html>
<html lang="en">
<head>
<meta charset="utf-8">
<title>Kelvaro Business Card</title>
<link href="https://fonts.googleapis.com/css2?family=Open+Sans:wght@400;600;700&display=swap" rel="stylesheet">
<style>
  :root {
    --brand-blue: #1a5fae;
    --brand-red: #ed282f;
    --ink: #2b2b2b;
    --rule: #333333;
    --paper: #ffffff;
    --backdrop: #ecebe8;
  }
  * { margin: 0; padding: 0; box-sizing: border-box; }
  html, body {
    width: 1200px; height: 1000px; overflow: hidden;
    background: var(--backdrop);
    font-family: "Open Sans", Arial, sans-serif;
  }
  .card {
    position: absolute; left: 265px; width: 666px; height: 397px;
    box-shadow: 0 2px 8px rgba(0,0,0,0.18);
  }
  .card--front { top: 73px; background: var(--paper); }
  .card--back { top: 533px; background: var(--brand-blue); }

  .wordmark {
    position: absolute; font-weight: 700; letter-spacing: -1px; line-height: 1;
  }
  .card--front .wordmark {
    left: 40px; top: 152px; font-size: 88px; color: var(--brand-blue);
  }
  .card--back .wordmark {
    left: 0; right: 0; top: 140px; text-align: center;
    font-size: 100px; color: var(--paper);
  }

  .person { position: absolute; left: 405px; top: 84px; }
  .person__name { font-size: 21px; font-weight: 700; color: var(--brand-blue); line-height: 1.25; }
  .person__title { font-size: 16px; color: var(--ink); line-height: 1.2; }

  .divider {
    position: absolute; left: 405px; right: 0; top: 150px;
    border-top: 1.5px solid var(--rule);
  }

  .address {
    position: absolute; left: 405px; top: 168px;
    font-size: 16px; line-height: 22px; color: var(--ink);
  }

  .contacts { position: absolute; left: 405px; top: 221px; list-style: none; }
  .contacts__item {
    display: flex; align-items: center; gap: 8px;
    font-size: 16px; line-height: 23px; color: var(--ink);
  }
  .contacts__icon { width: 15px; height: 15px; fill: var(--brand-blue); flex: none; }

  .card__url {
    position: absolute; left: 0; right: 0; top: 346px; text-align: center;
    font-size: 16px; letter-spacing: 1px; color: var(--paper);
  }
</style>
</head>
<body>
  <section class="card card--front">
    <div class="wordmark">Kelvaro</div>

    <div class="person">
      <div class="person__name">Tobias Vrenholt</div>
      <div class="person__title">CEO</div>
    </div>
    <div class="divider"></div>

    <address class="address" style="font-style:normal">
      4870 Larkmoor Ave., Suite C.<br>
      Fairhaven, OR. 97402
    </address>

    <ul class="contacts">
      <li class="contacts__item">
        <svg class="contacts__icon" viewBox="0 0 16 16" aria-hidden="true"><path d="M1 6c0-2 3-3 7-3s7 1 7 3v1h-3V5.5C11 5 9.5 5 8 5s-3 0-4 .5V7H1z"/><path d="M3 8h10l1 6H2z"/></svg>
        + 000 000 0000
      </li>
      <li class="contacts__item">
        <svg class="contacts__icon" viewBox="0 0 16 16" aria-hidden="true"><rect x="4" y="1" width="8" height="4"/><rect x="1" y="6" width="14" height="6" rx="1"/><rect x="4" y="10" width="8" height="5" fill="#fff" stroke="currentColor"/><rect x="4.5" y="10.5" width="7" height="4.5"/></svg>
        + 000 000 0000
      </li>
      <li class="contacts__item">
        <svg class="contacts__icon" viewBox="0 0 16 16" aria-hidden="true"><path d="M1 3h14v10H1z"/><path d="M1.5 3.5L8 9l6.5-5.5" fill="none" stroke="#fff" stroke-width="1.3"/></svg>
        info@kelvaro.com
      </li>
      <li class="contacts__item">
        <svg class="contacts__icon" viewBox="0 0 16 16" aria-hidden="true"><circle cx="8" cy="8" r="7"/><path d="M1 8h14M8 1c-3 3-3 11 0 14M8 1c3 3 3 11 0 14" fill="none" stroke="#fff" stroke-width="1"/></svg>
        www.kelvaro.com
      </li>
    </ul>
  </section>

  <section class="card card--back">
    <div class="wordmark">Kelvaro</div>
    <div class="card__url">www.kelvaro.com</div>
  </section>
</body>
</html>
```